Lumara Health & Wellness Business Card Design

We would like to create business cards matching with our new logo design. The card should be professional looking but still have a playful side and something that would be eye catching. We are planing to open a luxury medical spa and looking to create a design based on this new logo. We are looking for a design that shows off luxury but not be gold in color. Also, while we are a more female oriented medical center we do have men that come in for our services and it should be be too feminine.

Target Market(s)

Health & Wellness. Medical patients. Luxury spa

Industry/Entity Type

Health And Wellness

Contact Information for Business Card

It should have the logo design in the front of card and back of card should have our contact information. Our current colors are peach/ coral, teal, and gray. We are looking for a modern looking design.

Font styles to use
Script

Colors
32a6d6
e667a6
86cfc6
fece3e

Requirements
Must have
• It should have our logo design. We would prefer to have a more modern look to the card.
Nice to have
• Eye-Catching Design on the personable side but still classy.
Should not have
• At this point we are looking for the best design. It should not have color purple.

```html
<!DOCTYPE html>
<html lang="en">
<head>
<meta charset="utf-8">
<title>Lumara Health &amp; Wellness — Business Card</title>
<link rel="stylesheet" href="https://fonts.googleapis.com/css2?family=Arimo:wght@400&family=Kaushan+Script&display=swap">
<style>
  :root {
    --page-bg: #e9e7e4;
    --card-white: #ffffff;
    --card-black: #000000;
    --accent-blue: #32a6d6;
    --text-light: #ffffff;
    --text-dark: #111111;
  }
  * { margin: 0; padding: 0; box-sizing: border-box; }
  html, body {
    width: 1200px;
    height: 902px;
    overflow: hidden;
    background: var(--page-bg);
  }
  .canvas {
    position: relative;
    width: 1200px;
    height: 902px;
  }
  .card {
    position: absolute;
    left: 100px;
    top: 165px;
    width: 1000px;
    height: 572px;
    border-radius: 24px;
    overflow: hidden;
    background: var(--card-white);
    box-shadow: 0 10px 30px rgba(0,0,0,0.18);
    font-family: "Arimo", Arial, sans-serif;
  }
  .card-shapes {
    position: absolute;
    inset: 0;
  }
  .contact-panel {
    position: absolute;
    left: 65px;
    top: 120px;
    color: var(--text-light);
  }
  .holder-name {
    font-family: "Kaushan Script", cursive;
    font-size: 44px;
    line-height: 1;
    color: var(--text-light);
  }
  .holder-role {
    font-size: 22px;
    color: var(--accent-blue);
    margin-top: 0;
  }
  .address {
    margin-top: 74px;
    font-size: 21px;
    line-height: 29px;
  }
  .contact-list {
    list-style: none;
    margin-top: 20px;
  }
  .contact-item {
    display: flex;
    align-items: center;
    gap: 8px;
    font-size: 21px;
    height: 32px;
  }
  .contact-icon {
    width: 28px;
    height: 28px;
    flex: none;
  }
  .brand {
    position: absolute;
    left: 560px;
    top: 0;
    width: 440px;
    height: 572px;
    display: flex;
    flex-direction: column;
    align-items: center;
    justify-content: center;
    color: var(--text-dark);
    font-family: "Arimo", Arial, sans-serif;
    font-weight: 400;
  }
  .brand-name {
    font-size: 62px;
    line-height: 1;
  }
  .brand-tagline {
    font-size: 25px;
    margin-top: 10px;
  }
</style>
</head>
<body>
<main class="canvas">
  <section class="card">
    <svg class="card-shapes" width="1000" height="572" viewBox="0 0 1000 572" aria-hidden="true">
      <path d="M0 0 H522 Q396 286 522 572 H0 Z" fill="var(--card-black)"/>
      <path d="M534 0 Q408 286 534 572" fill="none" stroke="var(--accent-blue)" stroke-width="5"/>
      <circle cx="0" cy="158" r="26" fill="var(--accent-blue)"/>
    </svg>

    <div class="contact-panel">
      <p class="holder-name">Evan Carter</p>
      <p class="holder-role">Owner</p>
      <p class="address">PO BOX 482, Juniper Road<br>Suite 5, Tempe AZ 85281</p>
      <ul class="contact-list">
        <li class="contact-item">
          <svg class="contact-icon" viewBox="0 0 28 28" aria-hidden="true">
            <circle cx="14" cy="14" r="13" fill="var(--accent-blue)"/>
            <circle cx="14" cy="14" r="10.5" fill="none" stroke="var(--card-black)" stroke-width="1"/>
            <path d="M10 8 l3 0 l1 4 l-2 1.5 q1.5 3 4 4.5 l1.5 -2 l4 1 l0 3 q-8 1 -11.5 -12 z" fill="var(--card-black)"/>
          </svg>
          555.014.2378
        </li>
        <li class="contact-item">
          <svg class="contact-icon" viewBox="0 0 28 28" aria-hidden="true">
            <circle cx="14" cy="14" r="13" fill="var(--accent-blue)"/>
            <circle cx="14" cy="14" r="10.5" fill="none" stroke="var(--card-black)" stroke-width="1"/>
            <rect x="8" y="9.5" width="12" height="9" fill="none" stroke="var(--card-black)" stroke-width="1.6"/>
            <path d="M8 9.5 L14 15 L20 9.5" fill="none" stroke="var(--card-black)" stroke-width="1.6"/>
          </svg>
          hello@lumaraspa.com
        </li>
        <li class="contact-item">
          <svg class="contact-icon" viewBox="0 0 28 28" aria-hidden="true">
            <circle cx="14" cy="14" r="13" fill="var(--accent-blue)"/>
            <circle cx="14" cy="14" r="10.5" fill="none" stroke="var(--card-black)" stroke-width="1"/>
            <circle cx="14" cy="14" r="6.5" fill="none" stroke="var(--card-black)" stroke-width="1.4"/>
            <ellipse cx="14" cy="14" rx="3" ry="6.5" fill="none" stroke="var(--card-black)" stroke-width="1.2"/>
            <path d="M7.5 14 H20.5 M8.5 11 H19.5 M8.5 17 H19.5" stroke="var(--card-black)" stroke-width="1.1"/>
          </svg>
          www.lumaraspa.com
        </li>
      </ul>
    </div>

    <div class="brand">
      <p class="brand-name">Lumara</p>
      <p class="brand-tagline">Health &amp; Wellness</p>
    </div>
  </section>
</main>
</body>
</html>
```